UK Supplement Company Needs a Label for Diet Protein Powder

We need a new, modern and fresh design for our Diet Protein Powder. Our protein powder is packaged in black plastic tubs (photo attached) and needs an attractive label. We would like to see designs that grab attention and look professional. We're very open to ideas. The label should be 88mm x 365mm. We also prefer PSD format where possible. These alterations could be made once your design is chosen. Have attached photo of our shake ingredients/benefits.
Updates

Need extra days to review

Target Market(s)

Slimmers

Industry/Entity Type

Health And Wellness

Font styles to use
Serif
Sans Serif

Colors

Designer to choose colors to be used in the design.

Requirements
Must have
• Clean, Modern and Professional Look. Eye catching. The flavour, we offer 6 flavours so this must be something we can edit (Flavours are Banana, Chocolate, Chocolate Mint, Strawberry, Toffee and Vanilla).
Nice to have
• Our logo, this can be ZAVELTO Nutrition or just ZAVELTO. Our logo files are attached.
Should not have
• We do not want to see people (faces or bodies) on the design.

```html
<!DOCTYPE html>
<html lang="en">
<head>
<meta charset="utf-8">
<title>ZAVELTO Diet Protein Powder – Flavour Labels</title>
<link href="https://fonts.googleapis.com/css2?family=Barlow+Condensed:wght@500;600;700&family=Barlow:wght@700&display=swap" rel="stylesheet">
<style>
  :root {
    --page: #ffffff;
    --label-black: #141414;
    --badge-green: #b8d435;
    --flavour-green: #b5d334;
    --ink-dark: #151515;
    --vanilla-a: #e9c48c; --vanilla-b: #f7dfb3;
    --choc-a: #5a2f14;    --choc-b: #6e3a1a;
    --straw-a: #e0139a;   --straw-b: #f21aa6;
    --toffee-a: #c7682f;  --toffee-b: #e09a55;
    --mint-a: #1fa58c;    --mint-b: #2ed8b8;
    --banana-a: #f0c90d;  --banana-b: #f7e400;
  }
  * { box-sizing: border-box; margin: 0; padding: 0; }
  html, body { width: 1200px; height: 1200px; overflow: hidden; background: var(--page); }
  .range {
    width: 1200px; height: 1200px;
    display: grid;
    grid-template-columns: repeat(3, 340px);
    grid-template-rows: repeat(2, 500px);
    column-gap: 40px; row-gap: 60px;
    padding: 70px 50px;
  }
  .label {
    position: relative;
    background: var(--label-black);
    border-radius: 10px;
    overflow: hidden;
    font-family: "Barlow Condensed", sans-serif;
  }
  .label__band {
    position: absolute; left: 0; top: 0; width: 100%; height: 290px;
    background: linear-gradient(90deg, var(--a), var(--b) 50%, var(--a));
    clip-path: polygon(0 0, 100% 0, 100% 72%, 50% 100%, 0 72%);
  }
  .brand {
    position: absolute; left: 50%; top: 0; transform: translateX(-50%);
    width: 124px; height: 76px; background: var(--label-black);
    display: flex; flex-direction: column; align-items: center; justify-content: center;
    color: #fff;
  }
  .brand__name { font-family: "Barlow", sans-serif; font-weight: 700; font-size: 21px; letter-spacing: -0.3px; line-height: 1; }
  .brand__sub { font-size: 6px; letter-spacing: 2.4px; margin-top: 4px; font-weight: 500; }
  .title {
    position: absolute; top: 100px; width: 100%; text-align: center;
    color: var(--title, var(--ink-dark)); font-weight: 700; line-height: 0.9;
  }
  .title__top { display: block; font-size: 40px; letter-spacing: 0.5px; }
  .title__main { display: block; font-size: 62px; letter-spacing: 1px; }
  .flavour {
    position: absolute; top: 300px; width: 100%; text-align: center;
    color: var(--flavour-green); font-size: 32px; font-weight: 600;
  }
  .rule {
    position: absolute; top: 352px; left: 0; width: 100%; height: 3px;
    background: var(--rule, var(--b));
  }
  .badges {
    position: absolute; top: 380px; width: 100%;
    display: flex; justify-content: center; gap: 10px;
  }
  .badge {
    width: 48px; height: 48px; border-radius: 50%;
    border: 2px solid var(--badge-green);
    display: flex; flex-direction: column; align-items: center; justify-content: center;
    color: var(--badge-green); text-align: center;
  }
  .badge__value { font-size: 15px; font-weight: 600; line-height: 1; }
  .badge__value small { font-size: 9px; }
  .badge__name { font-size: 5px; line-height: 1.1; color: #fff; font-weight: 600; letter-spacing: 0.3px; }

  .label--vanilla    { --a: var(--vanilla-a); --b: var(--vanilla-b); }
  .label--chocolate  { --a: var(--choc-a);    --b: var(--choc-b); --title: #ffffff; --rule: #ffffff; }
  .label--strawberry { --a: var(--straw-a);   --b: var(--straw-b); }
  .label--toffee     { --a: var(--toffee-a);  --b: var(--toffee-b); }
  .label--mint       { --a: var(--mint-a);    --b: var(--mint-b); }
  .label--banana     { --a: var(--banana-a);  --b: var(--banana-b); }
</style>
</head>
<body>
<main class="range">
  <article class="label label--vanilla">
    <div class="label__band"></div>
    <div class="brand"><span class="brand__name">ZAVELTO</span><span class="brand__sub">NUTRITION</span></div>
    <h2 class="title"><span class="title__top">DIET PROTEIN</span><span class="title__main">POWDER</span></h2>
    <p class="flavour">Vanilla</p>
    <div class="rule"></div>
    <div class="badges">
      <div class="badge"><span class="badge__value">120<small>MG</small></span><span class="badge__name">GREEN TEA<br>EXTRACT</span></div>
      <div class="badge"><span class="badge__value">21<small>G</small></span><span class="badge__name">PROTEIN</span></div>
      <div class="badge"><span class="badge__value">120<small>MG</small></span><span class="badge__name">ACAI<br>BERRY</span></div>
      <div class="badge"><span class="badge__value">120<small>MG</small></span><span class="badge__name">CLA<br>POWDER</span></div>
    </div>
  </article>

  <article class="label label--chocolate">
    <div class="label__band"></div>
    <div class="brand"><span class="brand__name">ZAVELTO</span><span class="brand__sub">NUTRITION</span></div>
    <h2 class="title"><span class="title__top">DIET PROTEIN</span><span class="title__main">POWDER</span></h2>
    <p class="flavour">Chocolate</p>
    <div class="rule"></div>
    <div class="badges">
      <div class="badge"><span class="badge__value">120<small>MG</small></span><span class="badge__name">GREEN TEA<br>EXTRACT</span></div>
      <div class="badge"><span class="badge__value">21<small>G</small></span><span class="badge__name">PROTEIN</span></div>
      <div class="badge"><span class="badge__value">120<small>MG</small></span><span class="badge__name">ACAI<br>BERRY</span></div>
      <div class="badge"><span class="badge__value">120<small>MG</small></span><span class="badge__name">CLA<br>POWDER</span></div>
    </div>
  </article>

  <article class="label label--strawberry">
    <div class="label__band"></div>
    <div class="brand"><span class="brand__name">ZAVELTO</span><span class="brand__sub">NUTRITION</span></div>
    <h2 class="title"><span class="title__top">DIET PROTEIN</span><span class="title__main">POWDER</span></h2>
    <p class="flavour">Strawberry</p>
    <div class="rule"></div>
    <div class="badges">
      <div class="badge"><span class="badge__value">120<small>MG</small></span><span class="badge__name">GREEN TEA<br>EXTRACT</span></div>
      <div class="badge"><span class="badge__value">21<small>G</small></span><span class="badge__name">PROTEIN</span></div>
      <div class="badge"><span class="badge__value">120<small>MG</small></span><span class="badge__name">ACAI<br>BERRY</span></div>
      <div class="badge"><span class="badge__value">120<small>MG</small></span><span class="badge__name">CLA<br>POWDER</span></div>
    </div>
  </article>

  <article class="label label--toffee">
    <div class="label__band"></div>
    <div class="brand"><span class="brand__name">ZAVELTO</span><span class="brand__sub">NUTRITION</span></div>
    <h2 class="title"><span class="title__top">DIET PROTEIN</span><span class="title__main">POWDER</span></h2>
    <p class="flavour">Toffee</p>
    <div class="rule"></div>
    <div class="badges">
      <div class="badge"><span class="badge__value">120<small>MG</small></span><span class="badge__name">GREEN TEA<br>EXTRACT</span></div>
      <div class="badge"><span class="badge__value">21<small>G</small></span><span class="badge__name">PROTEIN</span></div>
      <div class="badge"><span class="badge__value">120<small>MG</small></span><span class="badge__name">ACAI<br>BERRY</span></div>
      <div class="badge"><span class="badge__value">120<small>MG</small></span><span class="badge__name">CLA<br>POWDER</span></div>
    </div>
  </article>

  <article class="label label--mint">
    <div class="label__band"></div>
    <div class="brand"><span class="brand__name">ZAVELTO</span><span class="brand__sub">NUTRITION</span></div>
    <h2 class="title"><span class="title__top">DIET PROTEIN</span><span class="title__main">POWDER</span></h2>
    <p class="flavour">Chocolate Mint</p>
    <div class="rule"></div>
    <div class="badges">
      <div class="badge"><span class="badge__value">120<small>MG</small></span><span class="badge__name">GREEN TEA<br>EXTRACT</span></div>
      <div class="badge"><span class="badge__value">21<small>G</small></span><span class="badge__name">PROTEIN</span></div>
      <div class="badge"><span class="badge__value">120<small>MG</small></span><span class="badge__name">ACAI<br>BERRY</span></div>
      <div class="badge"><span class="badge__value">120<small>MG</small></span><span class="badge__name">CLA<br>POWDER</span></div>
    </div>
  </article>

  <article class="label label--banana">
    <div class="label__band"></div>
    <div class="brand"><span class="brand__name">ZAVELTO</span><span class="brand__sub">NUTRITION</span></div>
    <h2 class="title"><span class="title__top">DIET PROTEIN</span><span class="title__main">POWDER</span></h2>
    <p class="flavour">Banana</p>
    <div class="rule"></div>
    <div class="badges">
      <div class="badge"><span class="badge__value">120<small>MG</small></span><span class="badge__name">GREEN TEA<br>EXTRACT</span></div>
      <div class="badge"><span class="badge__value">21<small>G</small></span><span class="badge__name">PROTEIN</span></div>
      <div class="badge"><span class="badge__value">120<small>MG</small></span><span class="badge__name">ACAI<br>BERRY</span></div>
      <div class="badge"><span class="badge__value">120<small>MG</small></span><span class="badge__name">CLA<br>POWDER</span></div>
    </div>
  </article>
</main>
</body>
</html>
```